Preferred pricing vendor

We are a plumbing company that has many services
-Boilers & Controls
-Plumbing & Heating
-HVAC & Refrigeration
-Preventative Maintenacne
-Gas fitting & Drain Cleaning

We primarily look after condo buildings, and our preferred service rates ($98, $93, or $88 depending on the contract) extend to all of our clients. So in essence, we look after the mechanical room and common equipment but our clients can call us in for drain cleaning or replacing a fixture in their suite. The discounted rates apply to the personal residence. We want a flyer to let them know they get a discount on our services. A one-pager we can send out to all of our contract clients.

Included source files for our letterhead and logo just so you can see the colours we go with.

Target Market(s)

Residential repairs, individual people, replacement of fixtures in-suite specific repairs

Requirements
Must have
• be colourful and attractive

```html
<!DOCTYPE html>
<html lang="en">
<head>
<meta charset="utf-8">
<title>Keystone Mechanical Inc – Plumbing Services Flyer</title>
<link href="https://fonts.googleapis.com/css2?family=Montserrat:wght@800;900&family=Oswald:wght@600&family=Roboto:wght@400;500;700&display=swap" rel="stylesheet">
<style>
  :root {
    --orange: #f05a28;
    --blue: #1f6fb8;
    --ink: #1c1c1c;
    --paper: #ffffff;
    --grey-band: #e4e4e4;
  }
  * { box-sizing: border-box; margin: 0; padding: 0; }
  html, body { width: 846px; height: 1200px; overflow: hidden; background: var(--paper); }
  .flyer {
    position: relative; width: 846px; height: 1200px; overflow: hidden;
    background: linear-gradient(180deg, #f4f5f6 0%, #ffffff 55%);
    font-family: "Roboto", Arial, sans-serif; color: var(--ink);
  }
  .hero-photo {
    position: absolute; left: 470px; top: 0; width: 376px; height: 648px;
    background: linear-gradient(160deg, #d9dde2 0%, #2a4fa8 45%, #c98f3a 62%, #2b4c9e 85%);
  }
  .brand {
    position: absolute; left: 39px; top: 170px; width: 455px;
    display: flex; align-items: center; justify-content: center; gap: 14px;
  }
  .brand-dot { width: 46px; height: 46px; border-radius: 50%; background: var(--orange); flex: none; }
  .brand-name {
    font-family: "Montserrat", Arial, sans-serif; font-weight: 900;
    color: var(--blue); font-size: 40px; line-height: 1.05; letter-spacing: 1px;
  }
  .brand-name span { display: block; font-size: 24px; letter-spacing: 3px; }
  .headline-box {
    position: absolute; left: 39px; top: 256px; width: 455px; height: 125px;
    background: var(--orange); color: #fff;
    font-family: "Montserrat", Arial, sans-serif; font-weight: 900;
    font-size: 56px; line-height: 54px; text-align: center; padding-top: 10px;
  }
  .services-title {
    position: absolute; left: 39px; top: 392px; width: 455px;
    font-family: "Oswald", Arial, sans-serif; font-weight: 600;
    color: var(--orange); font-size: 33px; text-align: center; letter-spacing: 0.5px;
  }
  .services-list {
    position: absolute; left: 38px; top: 437px; width: 457px; height: 211px;
    background: var(--blue); list-style: none; padding: 6px 0 0 10px;
  }
  .services-list li {
    display: flex; align-items: center; gap: 18px; height: 41px;
    color: #fff; font-size: 28px;
  }
  .service-icon {
    width: 34px; height: 34px; border-radius: 50%; background: #fff; flex: none;
    display: flex; align-items: center; justify-content: center;
  }
  .intro-band {
    position: absolute; left: 39px; top: 649px; width: 23px; height: 239px; background: var(--orange);
  }
  .intro-text {
    position: absolute; left: 86px; top: 666px; width: 706px;
    font-size: 18.5px; line-height: 22.5px; color: var(--ink);
  }
  .intro-text .rate { color: var(--orange); font-weight: 700; }
  .discount-note {
    position: absolute; left: 70px; top: 790px; width: 620px;
    font-family: "Montserrat", Arial, sans-serif; font-weight: 800; white-space: nowrap;
    color: var(--orange); font-size: 31px; line-height: 36px; text-align: center;
  }
  .discount-mark {
    position: absolute; left: 695px; top: 768px; width: 96px; height: 96px;
    border-radius: 50%; background: var(--orange);
  }
  .contact-panel {
    position: absolute; left: 39px; top: 888px; width: 807px; height: 282px; background: var(--grey-band);
  }
  .contact-band {
    position: absolute; left: 39px; top: 888px; width: 23px; height: 282px; background: var(--blue);
  }
  .technician-photo {
    position: absolute; left: 99px; top: 898px; width: 265px; height: 250px;
    background: radial-gradient(ellipse at 50% 55%, #2456b8 0%, #3b6cc7 45%, rgba(228,228,228,0) 75%);
  }
  .contact {
    position: absolute; left: 448px; top: 896px; width: 364px; text-align: center;
  }
  .address { font-size: 24px; line-height: 28px; color: #222; }
  .contact-title {
    font-family: "Montserrat", Arial, sans-serif; font-weight: 900;
    color: var(--blue); font-size: 56px; line-height: 50px; margin-top: 2px;
  }
  .email { font-size: 25px; line-height: 26px; letter-spacing: 4px; margin-top: 2px; color: #222; }
  .web { font-size: 26px; line-height: 26px; letter-spacing: 1px; color: #222; }
  .phone {
    font-family: "Roboto", Arial, sans-serif; font-weight: 700;
    font-size: 52px; line-height: 54px; color: var(--ink); letter-spacing: 1px;
  }
  .footer-blue { position: absolute; left: 0; top: 1170px; width: 555px; height: 30px; background: var(--blue); }
  .footer-orange { position: absolute; left: 564px; top: 1170px; width: 282px; height: 30px; background: var(--orange); }
</style>
</head>
<body>
<main class="flyer">
  <div class="hero-photo" role="img" aria-label="Plumber in blue overalls and red gloves holding a pipe wrench, wearing a tool belt"></div>

  <div class="brand">
    <div class="brand-dot"></div>
    <div class="brand-name">KEYSTONE<span>MECHANICAL INC</span></div>
  </div>

  <div class="headline-box">COMPANY<br>PLUMBING</div>
  <h2 class="services-title">SERVICES THAT WE PROVIDE</h2>

  <ul class="services-list">
    <li><span class="service-icon"><svg width="20" height="20" viewBox="0 0 20 20"><circle cx="10" cy="10" r="7" fill="none" stroke="#1f6fb8" stroke-width="2"/><line x1="10" y1="10" x2="14" y2="6" stroke="#1f6fb8" stroke-width="2"/></svg></span>Boilers &amp; Controls</li>
    <li><span class="service-icon"><svg width="20" height="20" viewBox="0 0 20 20"><rect x="5" y="3" width="10" height="14" rx="2" fill="#1f6fb8"/></svg></span>Plumbing &amp; Heating</li>
    <li><span class="service-icon"><svg width="20" height="20" viewBox="0 0 20 20"><path d="M3 10 L10 3 L17 10 V17 H3 Z" fill="none" stroke="#1f6fb8" stroke-width="2"/></svg></span>HVAC &amp; Refrigeration</li>
    <li><span class="service-icon"><svg width="20" height="20" viewBox="0 0 20 20"><line x1="4" y1="4" x2="16" y2="16" stroke="#1f6fb8" stroke-width="3"/><line x1="16" y1="4" x2="4" y2="16" stroke="#f05a28" stroke-width="3"/></svg></span>Preventative Maintenacne</li>
    <li><span class="service-icon"><svg width="20" height="20" viewBox="0 0 20 20"><line x1="10" y1="2" x2="10" y2="12" stroke="#1f6fb8" stroke-width="2"/><rect x="6" y="12" width="8" height="6" rx="2" fill="#1f6fb8"/></svg></span>Gas fitting &amp; Drain Cleaning</li>
  </ul>

  <div class="intro-band"></div>
  <p class="intro-text">We primarily look after condo buildings, and our preferred service rates (<span class="rate">$98</span>, <span class="rate">$93</span>, or <span class="rate">$88</span> depending on the contract) extend to all of our clients. So in essence, we look after the mechanical room and common equipment but our clients can call us in for drain cleaning or replacing a fixture in their suite.</p>

  <p class="discount-note">THE DISCOUNTED RATES APPLY<br>TO THE PERSONAL RESIDENCE.</p>
  <div class="discount-mark"></div>

  <div class="contact-panel"></div>
  <div class="contact-band"></div>
  <div class="technician-photo" role="img" aria-label="Smiling plumber in blue overalls sitting cross-legged with a plunger, gesturing to call"></div>

  <div class="contact">
    <p class="address">1280 Harbor View Road,<br>Suite 210 Bayside.</p>
    <p class="contact-title">PLUMBING<br>SERVICES</p>
    <p class="email">info@keystonemech.com</p>
    <p class="web">www.keystonemech.com</p>
    <p class="phone">555.214.7788</p>
  </div>

  <div class="footer-blue"></div>
  <div class="footer-orange"></div>
</main>
</body>
</html>
```